Bluestone Nine LLC Flyer Design

Marketing Materials for Real Estate Company. This flyer will be used to promote the company throughout the Commercial Real Estate business in the United States. The team has been together for 15 years. We are the middle guys between the Tenant, Broker, and the Owner. In the case of working with a Franchisor, we will be their Plug and Play leasing arm that will assist their new Franchisee's with their site selection, lease negotiations, design and construction management.

Target Market(s)

Real Estate Owners, Franchisor's, and Brokers

Font styles to use
Serif

Colors

Designer to choose colors to be used in the design.

Requirements
Must have
• The flyer must have......
• 1. The Best Leasing Machine On The Planet
• 2. Over the past 15 years our group has completed 4,492 lease transactions resulting in leasing 17,803,114 square feet in shopping centers across the United States.
• 3. Plug and Play Leasing Specialists. We handle the details between when the broker shows up with the space and the tenant and completing the lease negotiations, legal negotiations and documentation, and construction management to Certificate of Occupancy.
• 4. For Information Call Colette Varga at 555-014-2763 or Wendy Falk at 555-017-8302.
Nice to have
• National Tenants the we have completed transactions with....
• Pellmart, Fresh Basket, Harbor Pams, Vexo, Dunn, QV Rendo, Burrasco, Pattersons, Wrap Shack, Brewhorns, Summit Workout, ShipVo, Tredwell, PKN, Halvorsons, Q&L, Ledger Union Bank, Hen Haus-O, Lotus Kitchen, Furvo, Dex-Mart, Fieldly, and Orbit Theaters

```html
<!DOCTYPE html>
<html lang="en">
<head>
<meta charset="utf-8">
<title>Bluestone Nine LLC Flyer</title>
<link href="https://fonts.googleapis.com/css2?family=Tinos:wght@400;700&family=Gelasio:wght@700&display=swap" rel="stylesheet">
<style>
  :root {
    --teal: #178273;
    --orange: #f39a21;
    --green: #a6c95a;
    --navy: #1d4466;
    --white: #ffffff;
  }
  * { margin: 0; padding: 0; box-sizing: border-box; }
  html, body { width: 848px; height: 1200px; overflow: hidden; background: var(--white); }
  .flyer { position: relative; width: 848px; height: 1200px; overflow: hidden; background: var(--white); font-family: "Tinos", "Times New Roman", serif; }

  .brand-name {
    position: absolute; top: 34px; left: 0; width: 100%;
    text-align: center; color: var(--green);
    font-family: "Tinos", serif; font-weight: 700; font-size: 50px; letter-spacing: 2px;
  }

  .headline { position: absolute; left: 27px; top: 148px; color: var(--teal); line-height: 1; }
  .headline .best { display: block; color: var(--orange); font-weight: 700; font-size: 38px; }
  .headline .main { display: block; font-weight: 700; font-size: 49px; margin-top: 2px; letter-spacing: 0.5px; }
  .headline .sub { display: block; font-weight: 400; font-size: 31px; margin-top: 4px; letter-spacing: 1px; }

  .hero { position: absolute; left: 0; top: 0; }

  .about-title {
    position: absolute; left: 483px; top: 708px;
    color: var(--orange); font-weight: 700; font-size: 44px; letter-spacing: 2px;
  }

  .point { position: absolute; left: 118px; color: var(--navy); font-family: "Gelasio", Georgia, serif; font-weight: 700; font-size: 21px; letter-spacing: 1px; }
  .point-one { top: 786px; line-height: 34px; }
  .point-two { top: 907px; line-height: 28px; }
  .point-number {
    position: absolute; left: 40px; width: 41px; height: 41px; border-radius: 50%;
    background: var(--orange); color: var(--white);
    font-family: "Tinos", serif; font-weight: 700; font-size: 30px; line-height: 41px; text-align: center;
  }
  .number-one { top: 817px; }
  .number-two { top: 962px; }

  .transactions {
    position: absolute; left: 0; top: 1083px; width: 100%; height: 54px;
    background: var(--orange); color: var(--navy); text-align: center;
  }
  .transactions h2 { font-size: 13.5px; font-weight: 700; letter-spacing: 1px; margin-top: 5px; line-height: 16px; }
  .transactions p { font-size: 10.5px; font-weight: 700; line-height: 14px; letter-spacing: 0.2px; }

  .contact-bar {
    position: absolute; left: 0; top: 1137px; width: 100%; height: 63px;
    background: var(--teal); color: var(--orange);
    font-family: "Gelasio", Georgia, serif; font-weight: 700; font-size: 22px; letter-spacing: 1px;
  }
  .contact-bar .phone-icon { position: absolute; left: 46px; top: 10px; }
  .contact-bar span { position: absolute; top: 17px; }
  .c1-name { left: 110px; }
  .c1-num { left: 296px; }
  .c2-name { left: 465px; }
  .c2-num { left: 611px; }
</style>
</head>
<body>
<div class="flyer">

  <svg class="hero" width="848" height="780" viewBox="0 0 848 780">
    <defs>
      <linearGradient id="photoTone" x1="1" y1="0" x2="0.2" y2="1">
        <stop offset="0" stop-color="#3d4b63"/>
        <stop offset="0.45" stop-color="#5d6f8a"/>
        <stop offset="0.75" stop-color="#aab8cc"/>
        <stop offset="1" stop-color="#eef2f7"/>
      </linearGradient>
    </defs>
    <path class="hero-sweep" fill="var(--teal)"
      d="M157 413 C70 480 70 650 170 728 C230 775 320 785 400 745 L848 418 L848 396 L400 700 C320 745 230 735 175 690 C110 630 115 480 157 413 Z"/>
    <path class="hero-photo" role="img" aria-label="Photo of two business people shaking hands"
      fill="url(#photoTone)" stroke="var(--orange)" stroke-width="2.5"
      d="M848 133 L240 362 C150 400 118 470 120 545 C124 650 210 730 305 728 C345 727 385 712 420 690 L848 387 Z"/>
    <polygon class="badge" fill="var(--orange)" stroke="var(--white)" stroke-width="5"
      points="673,432 727,432 765,470 765,523 727,561 673,561 635,523 635,470"/>
    <circle role="img" aria-label="Globe illustration" cx="700" cy="496" r="44" fill="var(--teal)"/>
  </svg>

  <div class="brand-name">Bluestone Nine LLC</div>

  <h1 class="headline">
    <span class="best">BEST</span>
    <span class="main">LEASING MACHINE</span>
    <span class="sub">ON THE PLANET</span>
  </h1>

  <h2 class="about-title">ABOUT US</h2>

  <div class="point-number number-one">1</div>
  <p class="point point-one">Over the past 15 years our group has completed 4,492 lease<br>transactions resulting in leasing 17,803,114 square feet in<br>shopping centers across the United States.</p>

  <div class="point-number number-two">2</div>
  <p class="point point-two">Plug and Play Leasing Specialists. We handle the details<br>between when the broker shows up with the space and the<br>tenant and completing the lease negotiations,<br>legal negotiations and documentation, and construction<br>management to Certificate of Occupancy.</p>

  <section class="transactions">
    <h2>COMPLETE TRANSACTIONS</h2>
    <p>Pellmart, Fresh Basket, Harbor Pams, Vexo, Dunn, QV Rendo, Burrasco, Pattersons, Wrap Shack, Brewhorns, Summit Workout, ShipVo, Tredwell, PKN, Halvorsons, Q&amp;L,<br>Ledger Union Bank, Hen Haus-O, Lotus Kitchen, Furvo, Dex-Mart, Fieldly, and Orbit Theaters</p>
  </section>

  <footer class="contact-bar">
    <svg class="phone-icon" width="26" height="43" viewBox="0 0 26 43" aria-hidden="true">
      <rect x="1.5" y="1.5" width="23" height="40" rx="3" fill="none" stroke="var(--orange)" stroke-width="2.5"/>
      <line x1="9" y1="5.5" x2="17" y2="5.5" stroke="var(--orange)" stroke-width="1.5"/>
      <line x1="10" y1="37" x2="16" y2="37" stroke="var(--orange)" stroke-width="1.5"/>
    </svg>
    <span class="c1-name">Colette Varga</span>
    <span class="c1-num">555-014-2763</span>
    <span class="c2-name">Wendy Falk</span>
    <span class="c2-num">555-017-8302</span>
  </footer>

</div>
</body>
</html>
```